Hair dresser flyer for Air conditioning heat pumps A5

We require a flyer that is selling the benifits of air conditioning heat pumps which cools in summer and efficently heats in winter. Colour should be white background. Red and blue from logo to represent the Air conditioning Heat pump does heating and cooling and energy effient.

Target Market(s)

Hairdressor, Salons , barbers ,

Colors
0054AA
0677BA
7BADD7
CADEEF
E8F1F8
EB3D1F
EC4F4E
F09395
F8D3D4
FCEDEE

Requirements
Must have
• Cost from

```html
<!DOCTYPE html>
<html lang="en">
<head>
<meta charset="utf-8">
<title>Halloway – Air Conditioning Heat Pumps Flyer</title>
<link rel="stylesheet" href="https://fonts.googleapis.com/css2?family=Archivo+Black&family=Arvo:wght@400;700&family=Roboto:wght@400&display=swap">
<style>
  :root {
    --red: #EB3D1F;
    --orange: #E84E1B;
    --blue: #3AA5DE;
    --blue-deep: #0677BA;
    --ink: #1c1c1c;
    --white: #ffffff;
    --stage: #eeeeee;
    --rule: #bdbdbd;
  }
  * { box-sizing: border-box; margin: 0; padding: 0; }
  html, body { width: 719px; height: 1200px; overflow: hidden; }
  body { background: var(--stage); position: relative; font-family: "Arvo", serif; color: var(--ink); }

  .page {
    position: absolute; left: 155px; width: 569px; height: 815px;
    background: var(--white); transform: scale(0.717); transform-origin: top left;
    overflow: hidden; box-shadow: 0 6px 24px rgba(0,0,0,.12);
  }
  .page--front { top: 10px; }
  .page--back { top: 605px; }

  .photo { position: absolute; }

  /* Front */
  .hero-photo { left: 0; top: 0; width: 569px; height: 367px;
    background: linear-gradient(100deg, #f7f7f7 0%, #f1efec 38%, #d9cbbd 58%, #c7b3a2 75%, #e4e9ee 100%); }
  .brand { position: absolute; left: 352px; top: 34px; }
  .brand__name { font-family: "Arvo", serif; font-weight: 700; font-size: 30px; line-height: 32px; color: var(--ink); }
  .brand__tag { font-family: "Roboto", sans-serif; font-size: 11px; color: var(--ink); margin-top: 2px; }

  .save { position: absolute; left: 34px; top: 36px; font-family: "Archivo Black", sans-serif;
    font-size: 88px; line-height: 88px; letter-spacing: -3px; color: var(--red); }
  .pounds { position: absolute; left: 36px; top: 112px; font-family: "Archivo Black", sans-serif;
    font-size: 88px; line-height: 88px; letter-spacing: -2px; color: var(--blue); }
  .save-sub { position: absolute; left: 42px; top: 192px; width: 230px; font-weight: 700;
    font-size: 18.5px; line-height: 23px; }

  .offer-band { position: absolute; left: 0; top: 367px; width: 569px; height: 120px; background: var(--orange); }
  .offer-band__lead { position: absolute; left: 282px; top: 20px; color: var(--white); font-size: 15px; line-height: 19px; }
  .offer-band__price { position: absolute; left: 282px; top: 60px; color: var(--white); font-weight: 700; font-size: 25px; }

  .unit-photo { left: 22px; top: 408px; width: 214px; height: 186px;
    background: linear-gradient(160deg, #f0f0f0 0%, #5a5a5a 30%, #1a1a1a 65%, #e9e9e9 100%); }

  .benefits { position: absolute; left: 36px; top: 612px; list-style: none; }
  .benefits li { display: flex; align-items: center; gap: 11px; font-size: 11.5px; height: 20.6px; }
  .benefits svg { width: 13px; height: 13px; flex: none; }

  .info-box { position: absolute; left: 277px; top: 487px; width: 255px; height: 293px;
    background: var(--blue); border-radius: 0 0 14px 14px; padding: 16px 17px 0 20px;
    color: var(--white); font-size: 10px; line-height: 13.2px; }
  .info-box p + p { margin-top: 12px; }

  .foot-bar { position: absolute; left: 0; bottom: 0; height: 10px; width: 569px;
    background: linear-gradient(90deg, var(--blue) var(--split), var(--orange) var(--split)); }
  .page--front .foot-bar { --split: 288px; }
  .page--back .foot-bar { --split: 278px; }

  /* Back */
  .couple-photo { left: 0; top: 0; width: 569px; height: 367px;
    background: linear-gradient(100deg, #fbfbfb 0%, #f5f4f2 45%, #d6cfc8 62%, #b9b4b0 78%, #dfe6ec 100%); }
  .headline { position: absolute; left: 32px; top: 38px; color: var(--blue); font-weight: 700;
    font-size: 26px; line-height: 28px; }
  .intro { position: absolute; left: 32px; top: 109px; width: 236px; font-size: 14.5px; line-height: 19.8px; }

  .compare-band { position: absolute; left: 0; top: 367px; width: 569px; height: 130px; background: var(--orange); color: var(--white); }
  .compare { position: absolute; top: 30px; font-size: 13.5px; line-height: 18px; }
  .compare--heaters { left: 35px; }
  .compare--pump { left: 306px; }
  .compare__result { margin-top: 13px; font-size: 16px; }
  .compare__result span { margin-right: 14px; }
  .compare-divider { position: absolute; left: 268px; top: 28px; width: 1px; height: 72px; background: var(--white); }

  .salon-photo { top: 505px; height: 172px; }
  .salon-photo--front { left: 0; width: 185px; background: linear-gradient(135deg, #e8c9c0, #b9c8cf 60%, #3e6b3a); }
  .salon-photo--floor { left: 193px; width: 195px; background: linear-gradient(180deg, #d8d8d6, #9a948c 55%, #3c3a38); }
  .salon-photo--room { left: 396px; width: 173px; background: linear-gradient(135deg, #dfe3e6, #e6b9ad 55%, #bcb3a6); }

  .cta { position: absolute; left: 32px; top: 705px; width: 510px; font-size: 13.5px; line-height: 18px; }
  .cta-rule { position: absolute; left: 32px; top: 752px; width: 504px; height: 1px; background: var(--rule); }
  .contacts { position: absolute; left: 32px; top: 766px; width: 504px; display: flex; align-items: center; justify-content: space-between; font-size: 13px; }
  .contacts__item { display: flex; align-items: center; gap: 5px; }
  .contacts__item svg { width: 15px; height: 15px; }
  .contacts__phone { font-family: "Roboto", sans-serif; font-size: 21px; }
</style>
</head>
<body>

<section class="page page--front" aria-label="Flyer front">
  <div class="photo hero-photo" role="img" aria-label="Photo of a woman and child relaxing with a dog under a wall-mounted air conditioner"></div>

  <div class="brand">
    <div class="brand__name">Halloway</div>
    <div class="brand__tag">Temperature solutions for business.</div>
  </div>

  <div class="save">SAVE</div>
  <div class="pounds">£££</div>
  <p class="save-sub">on your Shops Heating costs And stay Cool in the Summer</p>

  <div class="offer-band">
    <p class="offer-band__lead">Energy- Efficient Air Conditioning<br>Heat Pumps installed</p>
    <p class="offer-band__price">from £1750 + Vat</p>
  </div>

  <div class="photo unit-photo" role="img" aria-label="Photo of a black wall-mounted air conditioning unit"></div>

  <ul class="benefits">
    <li><svg viewBox="0 0 14 14"><circle cx="7" cy="7" r="6" fill="none" stroke="#EB3D1F" stroke-width="1.3"/><path d="M4.2 7.2l2 2 3.6-4" fill="none" stroke="#EB3D1F" stroke-width="1.3"/></svg>Cools in Summer</li>
    <li><svg viewBox="0 0 14 14"><circle cx="7" cy="7" r="6" fill="none" stroke="#EB3D1F" stroke-width="1.3"/><path d="M4.2 7.2l2 2 3.6-4" fill="none" stroke="#EB3D1F" stroke-width="1.3"/></svg>Efficient Heats in Winter</li>
    <li><svg viewBox="0 0 14 14"><circle cx="7" cy="7" r="6" fill="none" stroke="#EB3D1F" stroke-width="1.3"/><path d="M4.2 7.2l2 2 3.6-4" fill="none" stroke="#EB3D1F" stroke-width="1.3"/></svg>More Productive staff</li>
    <li><svg viewBox="0 0 14 14"><circle cx="7" cy="7" r="6" fill="none" stroke="#EB3D1F" stroke-width="1.3"/><path d="M4.2 7.2l2 2 3.6-4" fill="none" stroke="#EB3D1F" stroke-width="1.3"/></svg>Increased Sales</li>
    <li><svg viewBox="0 0 14 14"><circle cx="7" cy="7" r="6" fill="none" stroke="#EB3D1F" stroke-width="1.3"/><path d="M4.2 7.2l2 2 3.6-4" fill="none" stroke="#EB3D1F" stroke-width="1.3"/></svg>Reduce cancellation in Summer</li>
    <li><svg viewBox="0 0 14 14"><circle cx="7" cy="7" r="6" fill="none" stroke="#EB3D1F" stroke-width="1.3"/><path d="M4.2 7.2l2 2 3.6-4" fill="none" stroke="#EB3D1F" stroke-width="1.3"/></svg>Filters and cleans the air</li>
    <li><svg viewBox="0 0 14 14"><circle cx="7" cy="7" r="6" fill="none" stroke="#EB3D1F" stroke-width="1.3"/><path d="M4.2 7.2l2 2 3.6-4" fill="none" stroke="#EB3D1F" stroke-width="1.3"/></svg>Reduced allergens &amp; Bugs</li>
    <li><svg viewBox="0 0 14 14"><circle cx="7" cy="7" r="6" fill="none" stroke="#EB3D1F" stroke-width="1.3"/><path d="M4.2 7.2l2 2 3.6-4" fill="none" stroke="#EB3D1F" stroke-width="1.3"/></svg>Reduce Humidity</li>
  </ul>

  <div class="info-box">
    <p>Air Conditioning Heat Pumps creates the ideal environment all year round for staff to be at there most productive and for consumers to spend more time and, accordingly, more money.</p>
    <p>Modern Air Conditioning Heat pumps are one of the most energy efficient forms of heating available and ideal for those looking for a simple cost effective way to heat and cool the space. They are easy to install and operate and can quickly provide with the comfort you need.</p>
    <p>Reduce cancelations and absences in the warm summer months with Cooling mode. With the warms temperatures inside hairdressers and salons and clients not wanting to sit in somewhere with extreme heat,</p>
  </div>

  <div class="foot-bar"></div>
</section>

<section class="page page--back" aria-label="Flyer back">
  <div class="photo couple-photo" role="img" aria-label="Photo of an older couple sitting together looking at a tablet in a warm living room"></div>

  <h1 class="headline">Reduce heating energy&nbsp; cost<br>by up to 75%</h1>
  <p class="intro">vs electric heating. Air conditioning heat pumps is a more efficient heating solution in comparison to a standard electric heaters which are still used in many businesses. This is because air conditioning produces more heat for the amount of electricity it takes to</p>

  <div class="compare-band">
    <div class="compare compare--heaters">
      <p>2 x 2kw Eleectic fan heaters<br>4kw Electricity input</p>
      <p class="compare__result"><span>=</span>4kw heat Output</p>
    </div>
    <div class="compare-divider"></div>
    <div class="compare compare--pump">
      <p>4kw Air Conditioning heat pump<br>1kw Electricty input</p>
      <p class="compare__result"><span>=</span>4kw Heat output</p>
    </div>
  </div>

  <div class="photo salon-photo salon-photo--front" role="img" aria-label="Photo of a salon shopfront with a service van outside"></div>
  <div class="photo salon-photo salon-photo--floor" role="img" aria-label="Photo of a salon floor with styling stations and ceiling air conditioning"></div>
  <div class="photo salon-photo salon-photo--room" role="img" aria-label="Photo of a pink salon room with a wall-mounted air conditioner"></div>

  <p class="cta">If you are interested in having air conditioning installed in your business, then give us a call on</p>
  <div class="cta-rule"></div>

  <div class="contacts">
    <span class="contacts__item contacts__phone">
      <svg viewBox="0 0 16 16"><path d="M4 1.5l2.2 2.6-1.3 1.6c.8 1.9 2.4 3.5 4.3 4.3l1.6-1.3 2.6 2.2-1.4 2.1C7.2 12.8 3.2 8.8 2 3.3z" fill="none" stroke="#1c1c1c" stroke-width="1.1" stroke-linejoin="round"/></svg>01632 960418</span>
    <span class="contacts__item">
      <svg viewBox="0 0 16 16"><circle cx="8" cy="8" r="6.3" fill="none" stroke="#1c1c1c" stroke-width="1"/><ellipse cx="8" cy="8" rx="2.8" ry="6.3" fill="none" stroke="#1c1c1c" stroke-width="1"/><path d="M1.7 8h12.6" stroke="#1c1c1c" stroke-width="1"/></svg>www.halloway.cool</span>
    <span class="contacts__item">
      <svg viewBox="0 0 16 16"><rect x="1.5" y="3.5" width="13" height="9" fill="none" stroke="#1c1c1c" stroke-width="1"/><path d="M1.5 3.5L8 9l6.5-5.5" fill="none" stroke="#1c1c1c" stroke-width="1"/></svg>info@halloway.cool</span>
  </div>

  <div class="foot-bar"></div>
</section>

</body>
</html>
```